Real estate agent website

I am a new real estate agent and in of a simple but powerful website that is linked to the local Multiple listing services (MLS). It should have a lending page that is connected to my customer relationship management (CRM) software. It must have an ability for potential customers to search for properties and be able to communicate with me easily.
Updates

Updates: The website themes must includes MLS-IDX integration with a grid layout and property slider so i can showcase featured properties. I also would like to have future where potential client can search and have alerts depending on a search criteria.

Industry/Entity Type

Real Estate

Coding

Coded - Design and coding required

Number of Pages Required

3 page

Requirements
Must have
• Home page, Resources page, About Me with contact me window page

```html
<!DOCTYPE html>
<html lang="en">
<head>
<meta charset="utf-8">
<title>Harborline Homes – Alex Morgan, Real Estate Agent</title>
<link href="https://fonts.googleapis.com/css2?family=Bodoni+Moda:wght@400;500;700;800&family=Montserrat:wght@300;400;500;600;700&family=Nunito+Sans:wght@300;400;600&display=swap" rel="stylesheet">
<style>
:root{
  --gold:#c8b459;
  --gold-dark:#b9a44a;
  --ink:#1d1d1d;
  --text:#3b3b3b;
  --muted:#8a8a8a;
  --line:#d6d6d6;
  --soft:#f3f3f3;
  --grid-bg:#f6f6f6;
  --white:#ffffff;
  --price:#e2876b;
  --dark:#161616;
  --accent-dot:#e02020;
  --serif:'Bodoni Moda', 'Didot', serif;
  --sans:'Montserrat', Arial, sans-serif;
  --body:'Nunito Sans', Arial, sans-serif;
}
*{box-sizing:border-box;margin:0;padding:0}
html,body{width:1200px;height:4223px;overflow:hidden}
body{position:relative;font-family:var(--sans);color:var(--text);background:var(--white)}
.abs{position:absolute}

/* Hero */
.hero{position:absolute;left:0;top:0;width:1200px;height:533px;overflow:hidden}
.hero-photo{position:absolute;inset:0;background:linear-gradient(180deg,#4f6585 0%,#62708a 25%,#6f5e4e 55%,#4c4a3a 80%,#3b4a2e 100%)}
.hero-shade{position:absolute;inset:0;background:linear-gradient(90deg,rgba(20,28,45,.55) 0%,rgba(20,28,45,.25) 55%,rgba(20,28,45,.15) 100%)}
.brand{position:absolute;left:152px;top:22px;font-family:var(--serif);font-weight:700;font-size:27px;color:var(--white)}
.nav{position:absolute;top:26px;left:533px;display:flex;gap:0;font-size:17px;font-weight:500;color:var(--white)}
.nav a{color:inherit;text-decoration:none;position:absolute;white-space:nowrap}
.phone{position:absolute;left:882px;top:21px;display:flex;align-items:center;gap:10px;color:var(--white);font-size:17px;font-weight:500}
.phone-badge{width:38px;height:38px;border-radius:50%;background:var(--white);display:flex;align-items:center;justify-content:center}
.hero-title{position:absolute;left:152px;top:192px;font-family:var(--serif);font-weight:700;font-size:50px;line-height:60px;color:var(--white)}
.hero-lead{position:absolute;left:152px;top:314px;width:400px;font-size:16.5px;line-height:26px;color:#f0f0f0;font-weight:400}

.search{position:absolute;left:700px;top:95px;width:353px;height:390px;background:#ececec;padding:24px 38px 0 38px}
.field-label{font-size:10px;color:#333;margin-bottom:7px;display:block}
.input{height:22px;border:1px solid #bdbdbd;background:var(--white);border-radius:3px;font-size:9px;color:#8c8c8c;padding:0 8px;display:flex;align-items:center;justify-content:space-between;margin-bottom:14px}
.pair{display:flex;gap:38px}
.pair > div{flex:1}
.search-btn{height:32px;background:var(--gold);color:var(--white);font-size:10px;font-weight:600;display:flex;align-items:center;justify-content:center;border-radius:2px;margin-top:6px}

/* About */
.about-photo{position:absolute;left:152px;top:605px;width:481px;height:376px;background:linear-gradient(120deg,#5b7b86 0%,#3f5a66 35%,#2b3438 60%,#5e6a70 100%)}
.about{position:absolute;left:688px;top:614px;width:360px}
.section-title{font-family:var(--serif);font-weight:800;font-size:27px;color:var(--ink);letter-spacing:.5px}
.about-sub{font-size:13px;color:var(--ink);margin-top:4px}
.about-body{margin-top:26px;font-size:13.4px;line-height:24px;color:#333}
.stats{display:flex;align-items:center;margin-top:28px}
.stat{display:flex;align-items:center;gap:12px}
.stat-num{font-size:30px;font-weight:500;color:var(--ink)}
.stat-label{font-size:13px;line-height:17px;color:#333}
.stat-divider{width:2px;height:42px;background:#333;margin:0 18px}

/* Featured */
.featured{position:absolute;left:0;top:1060px;width:1200px;height:612px;background:var(--soft)}
.center-title{position:absolute;left:0;width:1200px;text-align:center}
.slider-nav{position:absolute;top:142px;left:893px;display:flex;gap:26px;font-size:12.5px;font-weight:600;color:var(--ink)}
.feat-card{position:absolute;top:172px;width:381px;text-align:center}
.feat-photo{position:relative;height:259px}
.feat-photo .tag{position:absolute;right:42px;top:30px;background:#333;color:var(--white);font-size:12.5px;font-weight:600;padding:5px 8px}
.feat-photo .price{position:absolute;left:19px;bottom:14px;color:var(--white);font-size:18px}
.feat-title{margin-top:12px;font-size:20px;font-weight:600;color:var(--ink);white-space:nowrap}
.meta{display:inline-flex;align-items:center;gap:12px;color:#9a9a9a;font-size:13px;background:var(--white);padding:3px 8px;margin-top:10px}
.meta span{display:inline-flex;align-items:center;gap:4px}
.feat-label{font-size:9.5px;color:#333;margin-top:8px}
.dots{position:absolute;top:555px;left:580px;display:flex;gap:9px}
.dot{width:8px;height:8px;border-radius:50%;background:#d0d0d0}
.dot.on{background:var(--accent-dot)}

/* Recent */
.recent-row{position:absolute;left:146px;width:907px;height:230px;background:var(--grid-bg)}
.mini{position:absolute;top:16px;width:197px;height:197px;background:var(--white);box-shadow:0 1px 4px rgba(0,0,0,.08)}
.mini-photo{position:relative;height:140px}
.mini-photo .tag{position:absolute;right:6px;top:16px;background:rgba(40,40,40,.75);color:var(--white);font-size:6px;font-weight:600;padding:2px 4px}
.mini-title{margin:17px 0 0 13px;font-size:8.6px;font-weight:600;color:var(--ink);white-space:nowrap;overflow:hidden;width:174px;text-overflow:ellipsis}
.mini-foot{display:flex;justify-content:space-between;align-items:center;margin:8px 13px 0 13px}
.mini-price{font-size:9.5px;color:var(--price)}
.mini-meta{display:flex;gap:6px;font-size:7px;color:#9a9a9a}
.mini-meta span{display:inline-flex;align-items:center;gap:2px}
.ph-aerial{background:linear-gradient(135deg,#6f7a5e,#8e8f80 40%,#5d6a4e 70%,#9a9a90)}
.ph-villa{background:linear-gradient(180deg,#6f9ccb 0%,#c78a62 45%,#a9875f 70%,#7c8a55 100%)}
.ph-ranch{background:linear-gradient(180deg,#3f7fc9 0%,#5c6e5a 45%,#4d5a46 75%,#7d7b6c 100%)}
.ph-condo{background:linear-gradient(180deg,#bcd3e8 0%,#d7d8d2 40%,#8e9a80 70%,#9aa19a 100%)}
.ph-white{background:linear-gradient(180deg,#c8ccd2 0%,#e4e2dc 40%,#5f6c4a 80%,#4a5a35 100%)}
.ph-stone{background:linear-gradient(180deg,#4f5d48 0%,#7a7f80 40%,#50584a 75%,#3d4436 100%)}

/* Services */
.services{position:absolute;left:0;top:2365px;width:1200px;height:464px;background:var(--gold)}
.services-title{position:absolute;left:162px;top:94px;font-family:var(--serif);font-weight:800;font-size:23px;color:var(--ink)}
.service{position:absolute;width:250px}
.service-icon{position:absolute;left:-52px;top:-6px}
.service h3{font-size:16.5px;font-weight:500;color:var(--ink)}
.service p{margin-top:12px;font-size:12.6px;line-height:18.5px;color:#2d2d2d}

/* Testimonials */
.t-title{position:absolute;left:0;top:2898px;width:1215px;text-align:center;font-family:var(--serif);font-size:37px;font-weight:400;color:var(--ink)}
.t-kicker{position:absolute;left:0;top:2955px;width:1215px;text-align:center;font-size:11px;letter-spacing:12px;color:var(--gold)}
.t-avatar{position:absolute;left:551px;top:2999px;width:111px;height:111px;border-radius:50%;background:radial-gradient(circle at 50% 40%,#d9c4b2 0%,#b8a08e 45%,#2a2a2a 80%)}
.t-quote{position:absolute;left:330px;top:3133px;width:555px;text-align:center;font-family:var(--body);font-size:15px;line-height:26px;color:#555;font-weight:300}
.t-by{position:absolute;left:0;top:3230px;width:1215px;text-align:center;font-family:var(--body);font-size:12px;color:#333}
.t-by b{font-weight:600}
.t-role{position:absolute;left:0;top:3252px;width:1215px;text-align:center;font-family:var(--body);font-size:12px;font-style:italic;color:#666}
.t-arrow{position:absolute;top:3140px}
.t-dots{position:absolute;top:3306px;left:579px;display:flex;gap:22px}
.t-dots i{width:4px;height:4px;border-radius:50%;background:#aaa;display:block}
.t-dots i.on{background:#333}

/* Contact */
.contact{position:absolute;left:0;top:3380px;width:1200px;height:714px;overflow:hidden}
.contact-photo{position:absolute;inset:0;background:linear-gradient(100deg,#3a3a3a 0%,#272727 30%,#1e1e1e 55%,#343434 80%,#2a2a2a 100%)}
.contact-shade{position:absolute;inset:0;background:rgba(10,10,10,.35)}
.agent{position:absolute;left:190px;top:120px;color:var(--white)}
.agent-name{font-family:var(--serif);font-size:24px;font-weight:500;letter-spacing:1px}
.agent-role{font-size:12.5px;color:var(--gold);margin-top:8px;font-weight:500}
.agent-area{font-size:13px;margin-top:64px;font-weight:500}
.agent-addr{font-size:13px;margin-top:10px;color:#e6e6e6}
.agent-line{display:flex;align-items:center;gap:12px;font-size:13px;color:#e6e6e6}
.form{position:absolute;left:556px;top:116px;width:464px;height:547px;background:var(--white);padding:34px 44px 0 44px}
.form .field-label{font-size:11px;color:#222;margin-bottom:5px}
.form .input{height:25px;border-radius:0;border:1px solid #c8c8c8;font-size:10.5px;margin-bottom:13px}
.form .pair{gap:24px}
.form .area{height:56px;border:1px solid #c8c8c8;font-size:10.5px;color:#8c8c8c;padding:6px 8px;margin-bottom:18px}
.form .submit{height:27px;background:var(--gold);color:var(--white);font-size:11px;font-weight:600;display:flex;align-items:center;justify-content:center;margin-top:16px}

.footer{position:absolute;left:0;top:4094px;width:1200px;height:129px;background:var(--dark);color:#e0e0e0;font-size:13px;text-align:center;padding-top:52px}
</style>
</head>
<body>

<header class="hero">
  <div class="hero-photo" role="img" aria-label="Photo of a brick two-storey family house under a blue sky"></div>
  <div class="hero-shade"></div>
  <div class="brand">Harborline Homes</div>
  <nav class="nav">
    <a style="left:0">About</a>
    <a style="left:106px">Property</a>
    <a style="left:232px">Contact</a>
  </nav>
  <div class="phone">
    <span class="phone-badge">
      <svg width="20" height="20" viewBox="0 0 24 24"><path d="M6.6 10.8c1.4 2.8 3.8 5.1 6.6 6.6l2.2-2.2c.3-.3.7-.4 1-.2 1.1.4 2.3.6 3.6.6.6 0 1 .4 1 1V20c0 .6-.4 1-1 1C10.6 21 3 13.4 3 4c0-.6.4-1 1-1h3.5c.6 0 1 .4 1 1 0 1.3.2 2.5.6 3.6.1.3 0 .7-.2 1z" fill="none" stroke="#222" stroke-width="1.6"/></svg>
    </span>
    +1 555 010 2040
  </div>
  <h1 class="hero-title">Find Your Dream<br>House</h1>
  <p class="hero-lead">Lorem ipsum dolor sit amet consectetur. Est adipiscing euismod id tincidunt at mi nibh.</p>

  <form class="search">
    <label class="field-label">Location</label>
    <div class="input">Enter City Location</div>
    <label class="field-label">Property type</label>
    <div class="input">Enter City Location</div>
    <label class="field-label">Property type</label>
    <div class="input">House/condo <svg width="10" height="6" viewBox="0 0 10 6"><path d="M1 1l4 4 4-4" fill="none" stroke="#333" stroke-width="1.3"/></svg></div>
    <div class="pair">
      <div><label class="field-label">Min. Price</label><div class="input">$</div></div>
      <div><label class="field-label">Max. Price</label><div class="input">$</div></div>
    </div>
    <div class="pair">
      <div><label class="field-label">Beds</label><div class="input">Any <svg width="10" height="6" viewBox="0 0 10 6"><path d="M1 1l4 4 4-4" fill="none" stroke="#333" stroke-width="1.3"/></svg></div></div>
      <div><label class="field-label">Baths</label><div class="input">Any <svg width="10" height="6" viewBox="0 0 10 6"><path d="M1 1l4 4 4-4" fill="none" stroke="#333" stroke-width="1.3"/></svg></div></div>
    </div>
    <div class="search-btn">Search</div>
  </form>
</header>

<section>
  <div class="about-photo" role="img" aria-label="Portrait of the agent in a grey blazer in an office"></div>
  <div class="about">
    <h2 class="section-title">ABOUT</h2>
    <p class="about-sub">Your Name properties</p>
    <p class="about-body">Lorem ipsum dolor sit amet consectetur. Diam amet lacinia sed elit sed consectetur magna auctor. Sit imperdiet pellentesque maecenas ornare massa. Eu phasellus tincidunt cras ornare augue. Nulla in dignissim urna sit placerat lectus ut adipiscing. Id dui quam pellentesque nunc. Elit tristique volutpat lectus aenean. Aenean at id nisl morbi mauris urna. Amet scelerisque purus velit libero tellus sagittis sit nulla id. Ultrices amet proin risus ullamcorper.</p>
    <div class="stats">
      <div class="stat"><span class="stat-num">20+</span><span class="stat-label">Years of<br>experience</span></div>
      <div class="stat-divider"></div>
      <div class="stat"><span class="stat-num">100+</span><span class="stat-label">Properties<br>sold</span></div>
    </div>
  </div>
</section>

<section class="featured">
  <h2 class="section-title center-title" style="top:76px">FEATURED PROPERTIES</h2>
  <div class="slider-nav"><span>PREV</span><span>NEXT</span></div>

  <article class="feat-card" style="left:220px">
    <div class="feat-photo ph-white" role="img" aria-label="White cottage-style house with dark windows and front lawn">
      <span class="tag">FOR RENT</span><span class="price">$379,000</span>
    </div>
    <div class="feat-title">2140 MAPLE CREST WAY #12,OAKV...</div>
    <div class="meta">
      <span><svg width="16" height="11" viewBox="0 0 16 11"><path d="M1 10V2M1 6h14v4M4 6V3h5v3" fill="none" stroke="#999" stroke-width="1.2"/></svg>3</span>
      <span><svg width="12" height="13" viewBox="0 0 12 13"><path d="M2 12V2a1.5 1.5 0 0 1 3 0M1 7h10v2a3 3 0 0 1-3 3H4a3 3 0 0 1-3-3z" fill="none" stroke="#999" stroke-width="1.2"/></svg>2</span>
      <span><svg width="13" height="13" viewBox="0 0 13 13"><path d="M1 1v11h11zM4 6v3h3" fill="none" stroke="#999" stroke-width="1.2"/></svg>1918</span>
    </div>
    <div class="feat-label">RESIDENTIAL LEASE</div>
  </article>

  <article class="feat-card" style="left:616px">
    <div class="feat-photo ph-stone" role="img" aria-label="Grey stone house surrounded by tall trees">
      <span class="tag">FOR RENT</span><span class="price">$379,000</span>
    </div>
    <div class="feat-title">2140 MAPLE CREST WAY #12,OAKV...</div>
    <div class="meta">
      <span><svg width="16" height="11" viewBox="0 0 16 11"><path d="M1 10V2M1 6h14v4M4 6V3h5v3" fill="none" stroke="#999" stroke-width="1.2"/></svg>3</span>
      <span><svg width="12" height="13" viewBox="0 0 12 13"><path d="M2 12V2a1.5 1.5 0 0 1 3 0M1 7h10v2a3 3 0 0 1-3 3H4a3 3 0 0 1-3-3z" fill="none" stroke="#999" stroke-width="1.2"/></svg>2</span>
      <span><svg width="13" height="13" viewBox="0 0 13 13"><path d="M1 1v11h11zM4 6v3h3" fill="none" stroke="#999" stroke-width="1.2"/></svg>1918</span>
    </div>
    <div class="feat-label">RESIDENTIAL LEASE</div>
  </article>

  <div class="dots"><i class="dot on"></i><i class="dot"></i><i class="dot"></i></div>
</section>

<section>
  <h2 class="section-title center-title" style="top:1734px">RECENT PROPERTIES</h2>

  <div class="recent-row" style="top:1811px">
    <article class="mini" style="left:24px">
      <div class="mini-photo ph-aerial" role="img" aria-label="Aerial view of a wooded neighbourhood"><span class="tag">FOR SALE</span></div>
      <div class="mini-title">318 WILLOW BEND CIR ,FAIRHAVEN...</div>
      <div class="mini-foot"><span class="mini-price">$16,000</span></div>
    </article>
    <article class="mini" style="left:241px">
      <div class="mini-photo ph-villa" role="img" aria-label="Mediterranean-style apartment building with palm trees"><span class="tag">FOR RENT</span></div>
      <div class="mini-title">960 HARBOR VIEW CT #104,BAYP...</div>
      <div class="mini-foot"><span class="mini-price">$4,200</span><span class="mini-meta"><span>▭ 3</span><span>◫ 2</span><span>◺ 1918</span></span></div>
    </article>
    <article class="mini" style="left:457px">
      <div class="mini-photo ph-ranch" role="img" aria-label="Two-storey house with palm trees under blue sky"><span class="tag">FOR RENT</span></div>
      <div class="mini-title">2140 MAPLE CREST WAY #12,OAKV...</div>
      <div class="mini-foot"><span class="mini-price">$3,000</span><span class="mini-meta"><span>▭ 2</span><span>◫ 2</span><span>◺ 1502</span></span></div>
    </article>
    <article class="mini" style="left:674px">
      <div class="mini-photo ph-condo" role="img" aria-label="White townhouse complex with carports"><span class="tag">FOR RENT</span></div>
      <div class="mini-title">2751 CEDAR ROW DR #B7,LINDENW...</div>
      <div class="mini-foot"><span class="mini-price">$3,750</span><span class="mini-meta"><span>▭ 3</span><span>◫ 3</span><span>◺ 2025</span></span></div>
    </article>
  </div>

  <div class="recent-row" style="top:2060px">
    <article class="mini" style="left:24px">
      <div class="mini-photo ph-aerial" role="img" aria-label="Aerial view of a wooded neighbourhood"><span class="tag">FOR SALE</span></div>
      <div class="mini-title">318 WILLOW BEND CIR ,FAIRHAVEN...</div>
      <div class="mini-foot"><span class="mini-price">$16,000</span></div>
    </article>
    <article class="mini" style="left:241px">
      <div class="mini-photo ph-villa" role="img" aria-label="Mediterranean-style apartment building with palm trees"><span class="tag">FOR RENT</span></div>
      <div class="mini-title">960 HARBOR VIEW CT #104,BAYP...</div>
      <div class="mini-foot"><span class="mini-price">$4,200</span><span class="mini-meta"><span>▭ 3</span><span>◫ 2</span><span>◺ 1918</span></span></div>
    </article>
    <article class="mini" style="left:457px">
      <div class="mini-photo ph-ranch" role="img" aria-label="Two-storey house with palm trees under blue sky"><span class="tag">FOR RENT</span></div>
      <div class="mini-title">2140 MAPLE CREST WAY #12,OAKV...</div>
      <div class="mini-foot"><span class="mini-price">$3,000</span><span class="mini-meta"><span>▭ 2</span><span>◫ 2</span><span>◺ 1502</span></span></div>
    </article>
    <article class="mini" style="left:674px">
      <div class="mini-photo ph-condo" role="img" aria-label="White townhouse complex with carports"><span class="tag">FOR RENT</span></div>
      <div class="mini-title">2751 CEDAR ROW DR #B7,LINDENW...</div>
      <div class="mini-foot"><span class="mini-price">$3,750</span><span class="mini-meta"><span>▭ 3</span><span>◫ 3</span><span>◺ 2025</span></span></div>
    </article>
  </div>
</section>

<section class="services">
  <h2 class="services-title">MY SERVICES</h2>

  <div class="service" style="left:478px;top:107px">
    <svg class="service-icon" width="34" height="34" viewBox="0 0 34 34"><path d="M17 3L4 13h4v6h18v-6h4z" fill="#1d1d1d"/><path d="M6 24h8l4 3 8-3v6H6z" fill="#1d1d1d"/></svg>
    <h3>Real Estate Advisory</h3>
    <p>I specialize in real estate. I have a large amount of experience in the industry and I know how to find what you are looking for.</p>
  </div>
  <div class="service" style="left:808px;top:107px">
    <svg class="service-icon" width="34" height="34" viewBox="0 0 34 34"><path d="M19 4L9 12v8h20v-8z" fill="#1d1d1d"/><rect x="3" y="22" width="28" height="8" fill="#1d1d1d"/></svg>
    <h3>Property Management</h3>
    <p>I specialize in real estate. I have a large amount of experience in the industry and I know how to find what you are looking for.</p>
  </div>
  <div class="service" style="left:477px;top:256px">
    <svg class="service-icon" width="38" height="30" viewBox="0 0 38 30"><circle cx="10" cy="12" r="7" fill="none" stroke="#1d1d1d" stroke-width="4"/><path d="M16 14l18 10-2 4-4-2-2 3-3-2 1-3-9-5z" fill="#1d1d1d"/></svg>
    <h3>Property Leasing</h3>
    <p>Lorem ipsum dolor sit amet consectetur. Leo ornare ornare commodo nisi phasellus. Tempus nulla.</p>
  </div>
  <div class="service" style="left:808px;top:256px">
    <svg class="service-icon" width="34" height="34" viewBox="0 0 34 34"><path d="M17 3L2 16h4v15h22V16h4z" fill="#1d1d1d"/><circle cx="17" cy="21" r="5" fill="none" stroke="#c8b459" stroke-width="2"/></svg>
    <h3>Appraisals</h3>
    <p>Lorem ipsum dolor sit amet consectetur. Leo ornare ornare commodo nisi phasellus. Tempus nulla.</p>
  </div>
</section>

<section>
  <h2 class="t-title">Testimonials</h2>
  <p class="t-kicker">LOREM IPSUM DOLOR SIT AMET</p>
  <div class="t-avatar" role="img" aria-label="Client portrait"></div>
  <svg class="t-arrow" style="left:301px" width="10" height="14" viewBox="0 0 10 14"><path d="M8 1L2 7l6 6" fill="none" stroke="#999" stroke-width="1.3"/></svg>
  <svg class="t-arrow" style="left:903px" width="10" height="14" viewBox="0 0 10 14"><path d="M2 1l6 6-6 6" fill="none" stroke="#999" stroke-width="1.3"/></svg>
  <p class="t-quote">Really good Theme. We can't understand how we've been living without Harbor. They put together an incredible set of options- full of creative ideas that I've never seen in any other Theme.</p>
  <p class="t-by">by <b>Dana Whitfield</b></p>
  <p class="t-role">Marketing Manager, Brightpath Media</p>
  <div class="t-dots"><i class="on"></i><i></i><i></i></div>
</section>

<section class="contact">
  <div class="contact-photo" role="img" aria-label="Dimly lit modern living room interior"></div>
  <div class="contact-shade"></div>
  <div class="agent">
    <div class="agent-name">ALEX MORGAN</div>
    <div class="agent-role">REAL ESTATE AGEN</div>
    <div class="agent-area">Downtown | Coral Point</div>
    <div class="agent-addr">410 Palm Grove Avenue – Coral Point, FL 33012</div>
    <div class="agent-line" style="margin-top:26px">
      <svg width="18" height="18" viewBox="0 0 24 24"><path d="M6.6 10.8c1.4 2.8 3.8 5.1 6.6 6.6l2.2-2.2c.3-.3.7-.4 1-.2 1.1.4 2.3.6 3.6.6.6 0 1 .4 1 1V20c0 .6-.4 1-1 1C10.6 21 3 13.4 3 4c0-.6.4-1 1-1h3.5c.6 0 1 .4 1 1 0 1.3.2 2.5.6 3.6.1.3 0 .7-.2 1z" fill="none" stroke="#c8b459" stroke-width="1.6"/></svg>
      +1 (555) 014 7788
    </div>
    <div class="agent-line" style="margin-top:10px">
      <svg width="18" height="14" viewBox="0 0 18 14"><rect x="1" y="1" width="16" height="12" fill="none" stroke="#c8b459" stroke-width="1.4"/><path d="M1 1l8 7 8-7" fill="none" stroke="#c8b459" stroke-width="1.4"/></svg>
      alex@harborline.example
    </div>
  </div>

  <form class="form">
    <label class="field-label">Inquiry Type</label>
    <div class="input">Select <svg width="10" height="6" viewBox="0 0 10 6"><path d="M1 1l4 4 4-4" fill="none" stroke="#333" stroke-width="1.3"/></svg></div>
    <label class="field-label">Your information</label>
    <div class="input">i'm a ... <svg width="10" height="6" viewBox="0 0 10 6"><path d="M1 1l4 4 4-4" fill="none" stroke="#333" stroke-width="1.3"/></svg></div>
    <div class="pair">
      <div><label class="field-label">First name</label><div class="input">Enter your name</div></div>
      <div><label class="field-label">Last name</label><div class="input">Enter your last name</div></div>
    </div>
    <div class="pair">
      <div><label class="field-label">Email</label><div class="input">Enter your email</div></div>
      <div><label class="field-label">Phone</label><div class="input">Enter your phone</div></div>
    </div>
    <label class="field-label">Message</label>
    <div class="area">Message</div>
    <label class="field-label">Property Details</label>
    <div class="input">Select <svg width="10" height="6" viewBox="0 0 10 6"><path d="M1 1l4 4 4-4" fill="none" stroke="#333" stroke-width="1.3"/></svg></div>
    <div class="pair">
      <div><div class="input">Min Price</div></div>
      <div><div class="input">Minimum Size (sq ft)</div></div>
    </div>
    <div class="submit">Submit</div>
  </form>
</section>

<footer class="footer">© 2022 Alex Morgan Properties | All rights reserved</footer>

</body>
</html>
```